Larkmoor Business Card Design Project

Double side card , just the logo on oxford white background on one side , and the rest of the information on the other side..
the company name is : Larkmoor Continental General Trading LLC.
logo is already attached
the card to show in the info side: company name, employee name and position (job title) phone number, fax number, email address, P.O. box, Location (city and country)
deadline is already extended 4 all to have more time... thanks

```html
<!DOCTYPE html>
<html lang="en">
<head>
<meta charset="utf-8">
<title>Larkmoor Continental General Trading LLC. — Business Card</title>
<link href="https://fonts.googleapis.com/css2?family=Cinzel:wght@400&family=Crimson+Text:wght@400&display=swap" rel="stylesheet">
<style>
  :root {
    --backdrop: #e9e6e1;
    --card-white: #fbfbfa;
    --oxford-white: #f3f2ee;
    --band-grey: #4d4d4f;
    --ink-grey: #5a5a5c;
    --ink-dark: #333335;
    --brand-blue: #2a8fd0;
    --rule: #d5d5d5;
    --white: #ffffff;
  }
  * { box-sizing: border-box; margin: 0; padding: 0; }
  html, body {
    width: 1200px; height: 844px; overflow: hidden;
    background: var(--backdrop);
  }
  .canvas {
    width: 1200px; height: 844px;
    display: flex; align-items: center; justify-content: center; gap: 40px;
  }
  .card {
    width: 540px; height: 310px; border-radius: 16px; overflow: hidden;
    position: relative;
    box-shadow: 0 6px 18px rgba(0,0,0,0.18);
  }

  /* Shared brand lockup */
  .brand { display: flex; align-items: center; gap: 12px; }
  .brand-dot { width: 22px; height: 22px; border-radius: 50%; background: var(--brand-blue); flex: none; }
  .brand-name {
    font-family: "Cinzel", serif; font-weight: 400; font-size: 23px; line-height: 1.2;
    color: var(--ink-grey); letter-spacing: 0.5px;
  }
  .brand-name span { display: block; }

  /* Info side */
  .card-front { background: var(--card-white); display: flex; flex-direction: column; }
  .front-body { flex: 1; position: relative; padding: 32px 40px 0 56px; }
  .person { margin-top: 14px; margin-left: 34px; }
  .person-name {
    font-family: "Crimson Text", serif; font-size: 17px; letter-spacing: 0.5px;
    color: var(--brand-blue); text-transform: uppercase;
  }
  .person-title {
    font-family: "Crimson Text", serif; font-size: 13px; color: var(--ink-grey);
    margin-top: -2px;
  }
  .contacts {
    position: absolute; left: 56px; right: 40px; bottom: 18px;
    display: flex; align-items: flex-end;
  }
  .contact-col { display: flex; flex-direction: column; gap: 3px; }
  .contact-col.phones { width: 180px; }
  .contact-divider { width: 1px; height: 46px; background: var(--rule); margin-right: 26px; }
  .contact-line {
    display: flex; align-items: center; gap: 7px;
    font-family: "Crimson Text", serif; font-size: 14px; color: var(--ink-dark);
  }
  .contact-line svg { width: 14px; height: 14px; flex: none; }
  .address-band {
    height: 38px; background: var(--band-grey);
    display: flex; align-items: center; justify-content: center;
    font-family: "Crimson Text", serif; font-size: 14px; color: var(--white);
    letter-spacing: 0.3px;
  }

  /* Logo side */
  .card-back {
    background: var(--oxford-white);
    display: flex; align-items: center; justify-content: center;
  }
  .back-brand { gap: 14px; }
  .back-brand .brand-name { font-size: 27px; text-align: center; }
</style>
</head>
<body>
<main class="canvas">
  <section class="card card-front" aria-label="Business card, information side">
    <div class="front-body">
      <div class="brand">
        <span class="brand-dot"></span>
        <p class="brand-name"><span>Larkmoor Continental</span><span>General Trading LLC.</span></p>
      </div>
      <div class="person">
        <p class="person-name">Aldous Fenwick</p>
        <p class="person-title">General Manager</p>
      </div>
      <div class="contacts">
        <div class="contact-col phones">
          <p class="contact-line">
            <svg viewBox="0 0 14 14"><circle cx="7" cy="7" r="7" fill="var(--brand-blue)"/><path d="M4.5 3.8h1.6l.6 1.8-.9.7a5 5 0 0 0 1.9 1.9l.7-.9 1.8.6v1.6c-3.4.2-5.9-2.3-5.7-5.7z" fill="#fff"/></svg>
            63.582.7730
          </p>
          <p class="contact-line">
            <svg viewBox="0 0 14 14"><circle cx="7" cy="7" r="7" fill="var(--brand-blue)"/><rect x="4" y="5.5" width="6" height="4" fill="#fff"/><rect x="5" y="3.5" width="4" height="2" fill="#fff"/></svg>
            62.594.1209
          </p>
        </div>
        <span class="contact-divider"></span>
        <div class="contact-col">
          <p class="contact-line">
            <svg viewBox="0 0 14 14"><circle cx="7" cy="7" r="7" fill="var(--brand-blue)"/><rect x="3.8" y="4.6" width="6.4" height="4.8" fill="#fff"/><path d="M3.8 4.6 7 7.3l3.2-2.7" stroke="var(--brand-blue)" stroke-width=".8" fill="none"/></svg>
            info@larkmoorint.com
          </p>
          <p class="contact-line">
            <svg viewBox="0 0 14 14"><circle cx="7" cy="7" r="7" fill="var(--brand-blue)"/><circle cx="7" cy="7" r="3.4" fill="none" stroke="#fff" stroke-width=".9"/><path d="M3.6 7h6.8M7 3.6v6.8" stroke="#fff" stroke-width=".8"/></svg>
            www.larkmoorint.com
          </p>
        </div>
      </div>
    </div>
    <footer class="address-band">208 Harbour Lane, P.O. Box 452, Kelsford, B.C. V4K 1R8</footer>
  </section>

  <section class="card card-back" aria-label="Business card, logo side">
    <div class="brand back-brand">
      <span class="brand-dot"></span>
      <p class="brand-name"><span>Larkmoor Continental</span><span>General Trading LLC.</span></p>
    </div>
  </section>
</main>
</body>
</html>
```